Online medical reviews website needs banner advert!

We need banner advert templates for our website, www.wardplume.com. These should meet the technical requirements of our partner (uploaded).

Our groundbreaking website allows doctors in training to rate and review their training.

The adverts should use the same modern design language and colour scheme as our website. They should use the text 'Help a junior doctor make a big decision - rate your training!'.

Vector assets should be supplied, allowing us to use alternative text in future.
Updates

Industry/Entity Type

Healthcare

Font styles to use
Other font styles liked:
• Karla

Colors
3277b5
0555a3
ffffff

Requirements
Must have
• Similar design to our website. Should be elegant & modern. Must allow future text to be easily inserted.
Should not have
• Unrelated design.

```html
<!DOCTYPE html>
<html lang="en">
<head>
<meta charset="UTF-8">
<title>Ward Plume – Rate your Training</title>
<link href="https://fonts.googleapis.com/css2?family=Karla:wght@400;700;800&display=swap" rel="stylesheet">
<style>
  :root {
    --blue-light: #3277b5;
    --blue-deep: #0555a3;
    --blue-mid: #1d66ad;
    --white: #ffffff;
    --photo-warm: #e9dfd6;
    --photo-cool: #c9d3dc;
    --photo-shelf: #8aa3bd;
  }
  html, body {
    margin: 0;
    padding: 0;
    overflow: hidden;
    background: var(--white);
  }
  .banner {
    position: relative;
    width: 1200px;
    height: 309px;
    overflow: hidden;
    font-family: "Karla", Arial, sans-serif;
    background: var(--blue-light);
  }
  .banner__shapes {
    position: absolute;
    inset: 0;
    width: 1200px;
    height: 309px;
    display: block;
  }
  .banner__headline {
    position: absolute;
    left: 62px;
    top: 78px;
    margin: 0;
    color: var(--white);
    font-weight: 700;
    font-size: 43px;
    line-height: 47px;
    letter-spacing: 0.5px;
    text-transform: uppercase;
  }
  .banner__cta {
    position: absolute;
    left: 62px;
    top: 198px;
    width: 263px;
    height: 46px;
    display: flex;
    align-items: center;
    justify-content: center;
    background: var(--white);
    color: var(--blue-deep);
    border-radius: 5px;
    font-size: 21px;
    font-weight: 400;
    text-decoration: none;
    box-shadow: 0 2px 6px rgba(0, 0, 0, 0.12);
  }
</style>
</head>
<body>
  <div class="banner">
    <svg class="banner__shapes" viewBox="0 0 1200 309" xmlns="http://www.w3.org/2000/svg">
      <defs>
        <linearGradient id="lightPanel" x1="0" y1="0" x2="1" y2="1">
          <stop offset="0" stop-color="#3a7fbd"/>
          <stop offset="1" stop-color="#2a6fae"/>
        </linearGradient>
        <linearGradient id="deepPanel" x1="0" y1="0" x2="1" y2="1">
          <stop offset="0" stop-color="#0a5aa8"/>
          <stop offset="1" stop-color="#044f9a"/>
        </linearGradient>
        <linearGradient id="photoTones" x1="0" y1="0" x2="1" y2="0">
          <stop offset="0" stop-color="#b9c6d3"/>
          <stop offset="0.3" stop-color="#e4d8cf"/>
          <stop offset="0.6" stop-color="#d9b8a6"/>
          <stop offset="0.85" stop-color="#cfd6dd"/>
          <stop offset="1" stop-color="#aebfd0"/>
        </linearGradient>
      </defs>
      <rect class="panel-light" x="0" y="0" width="1200" height="309" fill="url(#lightPanel)"/>
      <polygon class="panel-deep" points="495,0 792,0 569,309 0,309 0,254" fill="url(#deepPanel)"/>
      <polygon class="photo-area" role="img"
               aria-label="Smiling young woman reading a red book in front of library bookshelves"
               points="792,0 1200,0 1200,309 569,309" fill="url(#photoTones)"/>
    </svg>

    <h1 class="banner__headline">Help a junior doctor<br>make a big decision -</h1>
    <a class="banner__cta" href="#">Rate your Training!</a>
  </div>
</body>
</html>
```